Burn Cream

We need to develop a (1) tube and (2) carton design. For a Lidocaine 2.5% burn cream.

This is a topical application cream. QUILMA is the Product Name. 1 oz.

Product

```html
<!DOCTYPE html>
<html lang="en">
<head>
<meta charset="utf-8">
<title>QUILMA Lidocaine 2.5% Burn Cream – Carton and Tube</title>
<link rel="stylesheet" href="https://fonts.googleapis.com/css2?family=Aleo:ital,wght@0,400;0,700;1,400&display=swap">
<style>
  :root {
    --bg: #e4e4e4;
    --navy: #004a97;
    --navy-dark: #0a3f86;
    --teal: #1ab0b8;
    --teal-band: #13c3cc;
    --silver: #d0d2d4;
    --white: #ffffff;
    --ink: #10386c;
    --cap: #f4f4f4;
  }
  * { margin: 0; padding: 0; box-sizing: border-box; }
  html, body { width: 1134px; height: 1200px; overflow: hidden; }
  body {
    background: var(--bg);
    font-family: "Aleo", Georgia, serif;
    position: relative;
  }

  /* Carton */
  .carton-front {
    position: absolute; left: 238px; top: 236px; width: 276px; height: 746px;
    background: var(--navy);
  }
  .carton-front .header {
    height: 198px; background: var(--silver); position: relative;
  }
  .brand {
    position: absolute; left: 52px; top: 128px;
    color: var(--navy-dark); font-size: 36px; line-height: 1; letter-spacing: -0.5px;
  }
  .tagline {
    position: absolute; left: 53px; top: 166px;
    color: var(--teal); font-size: 13px;
  }
  .product-name { position: absolute; left: 52px; top: 232px; font-size: 30px; line-height: 1.2; }
  .product-name .strength { color: var(--teal); display: block; }
  .product-name .type { color: var(--white); display: block; }
  .carton-copy {
    position: absolute; left: 48px; top: 502px; width: 200px;
    color: #d8e2f1; font-size: 14px; line-height: 1.32; font-style: italic;
  }
  .carton-copy p + p { margin-top: 16px; }
  .carton-copy strong { font-style: normal; font-weight: 700; color: var(--white); }

  .carton-side {
    position: absolute; left: 514px; top: 236px; width: 170px; height: 746px;
    background: var(--navy-dark);
  }
  .side-text {
    position: absolute; left: 100px; bottom: 36px;
    writing-mode: vertical-rl; transform: rotate(180deg);
    color: #c9d4e6; font-size: 9px; line-height: 1.5; height: 460px;
  }
  .side-text .batch { display: block; margin-left: 8px; }

  /* Tube */
  .tube { position: absolute; left: 628px; top: 238px; width: 310px; height: 752px; }
  .tube svg { position: absolute; left: 0; top: 0; }
  .tube-label {
    position: absolute; left: 62px; top: 110px; height: 360px;
    writing-mode: vertical-rl; transform: rotate(180deg);
    line-height: 1;
  }
  .tube-label .brand-line { color: var(--teal); font-size: 72px; display: block; margin-left: 4px; }
  .tube-label .line { color: var(--white); font-size: 54px; display: block; margin-left: 6px; }
  .tube-copy {
    position: absolute; left: 88px; top: 528px; width: 140px;
    color: var(--ink); font-size: 11.5px; line-height: 1.3; font-style: italic;
  }
  .tube-copy strong { font-style: normal; font-weight: 700; }
</style>
</head>
<body>

  <section class="carton-front">
    <div class="header">
      <div class="brand">QUILMA</div>
      <div class="tagline">Professional Skin Care</div>
    </div>
    <div class="product-name">
      <span class="strength">Lidocaine 2.5%</span>
      <span class="type">Burn Cream</span>
    </div>
    <div class="carton-copy">
      <p><strong>Ingredients:</strong> Lorem ipsum dolor sit amet, consectetur adipiscing elit.</p>
      <p><strong>How to use:</strong> Duis mattis malesuada enim, id nisl ullamcorper id. Lorem ipsum dolor sit amet, consectetur adipiscing elit.</p>
    </div>
  </section>

  <section class="carton-side">
    <div class="side-text">
      <span class="batch">℮30ml &nbsp; Chargen-Nr. 123-07</span>
      Lorem ipsum dolor sit amet, consectetur adipiscing elit. Quisque laoreet rutrum rhoncus. Sed gravida lacus enim, commodo laoreet odio ullamcorper non. Duis
    </div>
  </section>

  <section class="tube">
    <svg width="310" height="752" viewBox="0 0 310 752">
      <defs>
        <pattern id="ribs" width="5" height="30" patternUnits="userSpaceOnUse">
          <rect width="5" height="30" fill="#e2e2e2"/>
          <rect width="2" height="30" fill="#b9b9b9"/>
        </pattern>
      </defs>
      <rect class="crimp" x="0" y="0" width="310" height="28" fill="url(#ribs)"/>
      <polygon class="body" points="0,28 310,28 290,508 50,508" fill="var(--navy)"/>
      <polygon class="band" points="50,508 290,508 286,622 54,622" fill="var(--teal-band)"/>
      <path class="cap" d="M68,622 L278,622 L268,738 Q266,752 250,752 L96,752 Q80,752 78,738 Z" fill="var(--cap)"/>
    </svg>
    <div class="tube-label">
      <span class="brand-line">QUILMA</span>
      <span class="line">Lidocaine 2.5%</span>
      <span class="line">Burn Cream</span>
    </div>
    <div class="tube-copy">
      <strong>How to use:</strong> Duis mattis malesuada enim, id nisl ullamcorper id. Lorem ipsum dolor sit amet, consectetur adipiscing elit.
    </div>
  </section>

</body>
</html>
```